Brixo Tidy Yard Website

We need a website design for this new company. I've attached the company logo. This company is in the construction industry that provides general labor, maintenance and cleaning for construction sites. We want a clean and simple website that can be easy to navigate.

Target Market(s)

Construction industry

Industry/Entity Type

Construction

Number of Pages Required

2 page

Font styles to use
Sans Serif

```html
<!DOCTYPE html>
<html lang="en">
<head>
<meta charset="utf-8">
<title>Brixo Tidy Yard</title>
<link href="https://fonts.googleapis.com/css2?family=Roboto:wght@400;500;700&family=Lato:wght@400;700;900&display=swap" rel="stylesheet">
<style>
:root{
  --navy:#0a0a6b;
  --orange:#ff5a00;
  --grey-text:#666;
  --light:#eef0f3;
  --white:#fff;
}
*{margin:0;padding:0;box-sizing:border-box}
html,body{width:1200px;height:3015px;overflow:hidden}
body{position:relative;font-family:"Lato",sans-serif;background:var(--white);color:#333}
.abs{position:absolute}

/* header */
.site-header{left:0;top:0;width:1200px;height:88px;background:var(--white)}
.brand{left:78px;top:14px;width:126px;height:60px;display:flex;flex-direction:column;justify-content:center}
.brand span{font-family:"Roboto",sans-serif;font-weight:700;color:var(--navy);font-size:20px;line-height:22px}
.main-nav{left:330px;top:34px;font-family:"Roboto",sans-serif;font-size:15px;color:#222}
.main-nav a{text-decoration:none;color:inherit;position:absolute;white-space:nowrap}
.main-nav a.active{color:var(--orange)}
.estimate{left:940px;top:0;width:260px;height:88px;background:var(--orange);color:var(--white);font-family:"Roboto",sans-serif}
.estimate .label{position:absolute;left:58px;top:20px;font-size:14px}
.estimate .num{position:absolute;left:58px;top:40px;font-size:25px;font-weight:700}
.estimate svg{position:absolute;left:22px;top:28px}

/* hero */
.hero{left:0;top:88px;width:1200px;height:590px;background:linear-gradient(180deg,#8fa5bf 0%,#c9c3b0 45%,#b39b74 75%,#9a8466 100%)}
.hero-structure{left:560px;top:88px;width:640px;height:590px;background:linear-gradient(90deg,rgba(60,70,80,0),rgba(55,65,75,.75) 30%,rgba(50,58,66,.85))}
.hero-title{left:78px;top:300px;font-family:"Lato",sans-serif;font-weight:900;font-size:47px;color:var(--navy);letter-spacing:.5px}
.hero-band{left:78px;top:373px;width:414px;height:50px;background:var(--orange);color:var(--white);font-family:"Lato",sans-serif;font-weight:900;font-size:26px;line-height:50px;padding-left:18px}
.hero-dots{left:78px;top:458px;display:flex;gap:6px}
.hero-dots i{display:block;width:15px;height:15px;border-radius:50%;background:var(--white);border:2px solid #ddd}
.hero-dots i.on{background:var(--orange);border-color:var(--white)}

/* section heads */
.eyebrow{left:0;width:1200px;text-align:center;font-family:"Roboto",sans-serif;font-size:20px;color:var(--orange);letter-spacing:.5px}
.section-title{left:0;width:1200px;text-align:center;font-family:"Roboto",sans-serif;font-weight:700;font-size:42px;color:var(--navy)}

.intro-text{left:255px;width:690px;text-align:center;font-size:15px;line-height:27px;color:var(--grey-text)}
.btn{background:var(--orange);color:var(--white);font-family:"Lato",sans-serif;font-weight:700;font-size:19px;text-align:center}

/* services */
.services{left:0;top:1166px;width:1200px;height:572px;background:linear-gradient(90deg,#dfe3e8,#f2f3f5 50%,#e4e6ea)}
.service-photo{top:1342px;width:312px;height:292px}
.service-label{top:1588px;width:270px;height:82px;background:var(--orange);color:var(--white);padding:16px 22px}
.service-label h3{font-family:"Lato",sans-serif;font-weight:900;font-size:19px}
.service-label p{font-size:13px;margin-top:4px}

/* testimonial */
.testimonial{left:0;top:1738px;width:1200px;height:324px;background:var(--navy)}
.client-ring{left:166px;top:1788px;width:228px;height:228px;border-radius:50%;border:2px solid var(--white)}
.client-photo{left:180px;top:1802px;width:200px;height:200px;border-radius:50%;background:radial-gradient(circle,#6b5a50,#3a3f4a)}
.quote{left:454px;top:1844px;width:530px;font-size:14px;line-height:27px;color:var(--white)}
.qmark{font-family:"Roboto",sans-serif;font-weight:700;font-size:38px;color:var(--orange);line-height:1}
.client-name{left:940px;top:1964px;width:132px;text-align:right;font-family:"Roboto",sans-serif;font-weight:700;font-size:15px;color:var(--white)}
.client-name::before{content:"";display:inline-block;width:16px;height:2px;background:var(--orange);vertical-align:middle;margin-right:8px}

/* contact */
.contact-sub{left:0;width:1200px;text-align:center;font-family:"Roboto",sans-serif;font-weight:500;font-size:15px;color:#222;line-height:26px}
.field{left:330px;width:540px;height:48px;border:1px solid #e2e2e2;background:var(--white)}
.field span{position:absolute;left:22px;top:14px;font-size:13px;color:#777}
.field .ico{position:absolute;right:0;top:0;width:36px;height:100%;background:var(--navy);display:flex;align-items:center;justify-content:center}

/* footer */
.site-footer{left:0;top:2680px;width:1200px;height:272px;background:var(--navy)}
.footer-brand{left:108px;top:2744px;width:190px;text-align:center;font-family:"Roboto",sans-serif;font-weight:700;font-size:30px;line-height:36px;color:var(--white)}
.social{top:2844px;width:40px;height:40px;border-radius:50%}
.footer-head{top:2708px;font-family:"Roboto",sans-serif;font-weight:700;font-size:17px;color:var(--orange)}
.sitemap{left:344px;top:2744px;list-style:none;font-size:14px;color:#d8d8ee;line-height:29px}
.sitemap li::before{content:"";display:inline-block;width:5px;height:5px;border-radius:50%;background:var(--orange);margin-right:12px;vertical-align:middle}
.news-thumb{width:56px;height:56px;border-radius:50%;border:2px solid var(--white);background:linear-gradient(135deg,#c8cfd8,#7c8a9b)}
.news-text{width:170px;font-size:13px;line-height:23px;color:#d8d8ee}
.footer-contact{font-size:14px;color:#d8d8ee;line-height:23px}
.copyright{left:0;top:2952px;width:1200px;height:63px;background:var(--orange);color:var(--white);text-align:center;line-height:63px;font-size:13px}
</style>
</head>
<body>

<header class="site-header abs">
  <div class="brand abs"><span>BRIXO</span><span>TIDY YARD</span></div>
  <nav class="main-nav abs">
    <a class="active" style="left:0">HOME</a>
    <a style="left:78px">ABOUT</a>
    <a style="left:164px">SERVICES</a>
    <a style="left:270px">TESTIMONIAL</a>
    <a style="left:404px">NEWS</a>
    <a style="left:476px">CONTACT</a>
    <svg style="position:absolute;left:582px;top:2px" width="16" height="16" viewBox="0 0 16 16"><circle cx="6.5" cy="6.5" r="5" fill="none" stroke="#0a0a6b" stroke-width="2"/><line x1="10" y1="10" x2="15" y2="15" stroke="#0a0a6b" stroke-width="2"/></svg>
  </nav>
  <div class="estimate abs">
    <svg width="28" height="34" viewBox="0 0 24 24"><path fill="#fff" d="M6.6 10.8c1.4 2.8 3.8 5.1 6.6 6.6l2.2-2.2c.3-.3.7-.4 1-.2 1.1.4 2.3.6 3.6.6.6 0 1 .4 1 1V20c0 .6-.4 1-1 1C10.6 21 3 13.4 3 4c0-.6.4-1 1-1h3.5c.6 0 1 .4 1 1 0 1.3.2 2.5.6 3.6.1.3 0 .7-.2 1z"/></svg>
    <div class="label">Request a Estimate :</div>
    <div class="num">123 456 7890</div>
  </div>
</header>

<section>
  <div class="hero abs" role="img" aria-label="Photo of two construction workers in hard hats on a steel platform above a large building site"></div>
  <div class="hero-structure abs"></div>
  <h1 class="hero-title abs">WE ARE LEADERS IN</h1>
  <div class="hero-band abs">CONSTRUCTION INDUSTRY</div>
  <div class="hero-dots abs"><i></i><i class="on"></i><i></i><i></i><i></i></div>
</section>

<section>
  <div class="eyebrow abs" style="top:740px">WELCOME TO</div>
  <h2 class="section-title abs" style="top:768px">BRIXO TIDY YARD</h2>
  <p class="intro-text abs" style="top:838px">Lorem Ipsum is simply dummy text of the printing and typesetting industry. Lorem Ipsum has been the industry's standard dummy text ever since the 1500s, when an unknown printer took a galley of type and scrambled it to make a type specimen book.</p>
  <p class="intro-text abs" style="top:930px">It has survived not only five centuries, but also the leap into electronic typesetting, remaining essentially unchanged. It was popularised in the 1960s with the release of Varnel sheets containing Lorem Ipsum passages, and more recently with desktop publishing software like Quillset Pagewright including versions of Lorem Ipsum</p>
  <div class="btn abs" style="left:512px;top:1056px;width:176px;height:46px;line-height:46px">LEARN MORE</div>
</section>

<section>
  <div class="services abs"></div>
  <div class="eyebrow abs" style="top:1228px">WHAT WE DO</div>
  <h2 class="section-title abs" style="top:1256px">SERVICES WE PROVIDED</h2>

  <div class="service-photo abs" style="left:98px;background:linear-gradient(160deg,#e8d6a8,#8a7a60 60%,#4c4a48)" role="img" aria-label="Photo of tower cranes above high-rise buildings under construction"></div>
  <div class="service-photo abs" style="left:444px;background:linear-gradient(160deg,#cfd6de,#a8b4c0 50%,#6c7280)" role="img" aria-label="Photo of a worker holding a yellow hard hat with a tool belt"></div>
  <div class="service-photo abs" style="left:788px;background:linear-gradient(160deg,#d8dde3,#b9c0c8 55%,#e0c060)" role="img" aria-label="Photo of a cleaner with a mop, yellow bucket and spray bottle"></div>

  <div class="service-label abs" style="left:118px"><h3>GENERAL LABOR</h3><p>Lorem ipsum simple text of print</p></div>
  <div class="service-label abs" style="left:464px"><h3>MAINTENANCE</h3><p>Lorem ipsum simple text of print</p></div>
  <div class="service-label abs" style="left:808px"><h3>CLEANING</h3><p>Lorem ipsum simple text of print</p></div>
</section>

<section>
  <div class="testimonial abs"></div>
  <div class="client-ring abs"></div>
  <div class="client-photo abs" role="img" aria-label="Portrait photo of a smiling client"></div>
  <div class="abs qmark" style="left:424px;top:1842px">“</div>
  <p class="quote abs">Lorem Ipsum is simply dummy text of the printing and typesetting industry. Lorem Ipsum has been the industry's standard dummy text ever since the 1500s, when an unknown printer took a galley of type and scrambled it to make a type specimen book.</p>
  <div class="abs qmark" style="left:668px;top:1928px">”</div>
  <div class="client-name abs">CLIENT NAME</div>
</section>

<section>
  <div class="eyebrow abs" style="top:2122px;font-size:18px">KEEP IN TOUCH</div>
  <h2 class="section-title abs" style="top:2150px">CONTACT US</h2>
  <p class="contact-sub abs" style="top:2214px">If you have any Questions, Please do not Hesitate to send us a Message.<br>We aim to Reply Within 24 Hours.</p>

  <div class="field abs" style="top:2292px"><span>Name *</span><div class="ico"><svg width="12" height="12" viewBox="0 0 12 12"><circle cx="6" cy="3.5" r="2.8" fill="#fff"/><path d="M1 12c0-3.5 2.2-5 5-5s5 1.5 5 5z" fill="#fff"/></svg></div></div>
  <div class="field abs" style="top:2350px"><span>Email *</span><div class="ico"><svg width="13" height="10" viewBox="0 0 13 10"><rect width="13" height="10" fill="#fff"/><path d="M0 0l6.5 5L13 0" fill="none" stroke="#0a0a6b" stroke-width="1.2"/></svg></div></div>
  <div class="field abs" style="top:2408px"><span>Phone *</span><div class="ico"><svg width="13" height="13" viewBox="0 0 24 24"><path fill="#fff" d="M6.6 10.8c1.4 2.8 3.8 5.1 6.6 6.6l2.2-2.2c.3-.3.7-.4 1-.2 1.1.4 2.3.6 3.6.6.6 0 1 .4 1 1V20c0 .6-.4 1-1 1C10.6 21 3 13.4 3 4c0-.6.4-1 1-1h3.5c.6 0 1 .4 1 1 0 1.3.2 2.5.6 3.6.1.3 0 .7-.2 1z"/></svg></div></div>
  <div class="field abs" style="top:2466px;height:92px"><span>Message *</span><div class="ico"><svg width="16" height="13" viewBox="0 0 16 13"><ellipse cx="6" cy="5" rx="6" ry="4.5" fill="#fff"/><ellipse cx="11" cy="8" rx="5" ry="4" fill="#fff" stroke="#0a0a6b"/></svg></div></div>
  <div class="btn abs" style="left:514px;top:2566px;width:172px;height:52px;line-height:52px;font-family:'Roboto',sans-serif">SUBMIT</div>
</section>

<footer>
  <div class="site-footer abs"></div>
  <div class="footer-brand abs">BRIXO<br>TIDY YARD</div>
  <div class="social abs" style="left:136px;background:#1e2a7a"></div>
  <div class="social abs" style="left:184px;background:#1aa1e6"></div>
  <div class="social abs" style="left:232px;background:#c8302a"></div>

  <h4 class="footer-head abs" style="left:344px">SITEMAP</h4>
  <ul class="sitemap abs"><li>Home</li><li>About</li><li>Services</li><li>Testimonials</li><li>News</li><li>Contact</li></ul>

  <h4 class="footer-head abs" style="left:610px">News</h4>
  <div class="news-thumb abs" style="left:606px;top:2734px" role="img" aria-label="News thumbnail photo"></div>
  <p class="news-text abs" style="left:682px;top:2738px">lorem ipsum simple text of print type text</p>
  <div class="news-thumb abs" style="left:606px;top:2830px" role="img" aria-label="News thumbnail photo"></div>
  <p class="news-text abs" style="left:682px;top:2834px">lorem ipsum simple text of print type text</p>

  <h4 class="footer-head abs" style="left:874px">CONTACT US</h4>
  <svg class="abs" style="left:872px;top:2752px" width="14" height="20" viewBox="0 0 14 20"><path d="M7 0a7 7 0 0 1 7 7c0 5-7 13-7 13S0 12 0 7a7 7 0 0 1 7-7z" fill="#ff5a00"/><circle cx="7" cy="7" r="2.6" fill="#0a0a6b"/></svg>
  <p class="footer-contact abs" style="left:902px;top:2748px;width:200px">101 - lorem ipsum simple text of print type text</p>
  <svg class="abs" style="left:872px;top:2824px" width="15" height="15" viewBox="0 0 24 24"><path fill="#ff5a00" d="M6.6 10.8c1.4 2.8 3.8 5.1 6.6 6.6l2.2-2.2c.3-.3.7-.4 1-.2 1.1.4 2.3.6 3.6.6.6 0 1 .4 1 1V20c0 .6-.4 1-1 1C10.6 21 3 13.4 3 4c0-.6.4-1 1-1h3.5c.6 0 1 .4 1 1 0 1.3.2 2.5.6 3.6.1.3 0 .7-.2 1z"/></svg>
  <p class="footer-contact abs" style="left:902px;top:2820px;font-size:16px">123 456 7890</p>
  <svg class="abs" style="left:872px;top:2870px" width="15" height="15" viewBox="0 0 15 15"><rect x="0" y="3" width="15" height="12" rx="1" fill="#ff5a00"/><rect x="3" y="0" width="9" height="5" fill="#ff5a00"/><rect x="3" y="7" width="9" height="2" fill="#0a0a6b"/></svg>
  <p class="footer-contact abs" style="left:902px;top:2866px;font-size:16px">123 456 7890</p>
  <svg class="abs" style="left:872px;top:2906px" width="15" height="11" viewBox="0 0 15 11"><rect width="15" height="11" fill="#ff5a00"/><path d="M0 0l7.5 6L15 0" fill="none" stroke="#0a0a6b" stroke-width="1.3"/></svg>
  <p class="footer-contact abs" style="left:902px;top:2900px;font-size:13px">info@brixotidyyard.com</p>

  <div class="copyright abs">©BRIXOTIDYYARD -2019 All Right Reserved.</div>
</footer>

</body>
</html>
```